Survey App for phone users trying a new phone with Dual connectivity

Survey App Brief<br/>Design For an Android Survey App for users' feedback on Call, SMS, Data and Streaming Experience on their Mobile phones.<br/><br/>Purpose of the App<br/>To ensure that the user's experience is not impacted by the network switching between two network on the special mobile phones they newly started using.<br/><br/>App Requirements:<br/>First screen: The registration screen, where the user needs to enter the following:<br/>Name: text box<br/>Phone Number: text box<br/>Group Number : <br/><br/>An information text:<br/>By Registering I agree to participate in the Survey.<br/><br/>Register: Button<br/><br/>Start Screen - Survey screens (next time user open the App this will be the first screen):<br/>We need feedback for 4 indicators:<br/>Call Experience<br/>SMS Experience<br/>Data Experience<br/>Streaming Experience<br/><br/>Each Experience can be in the form of a questionnaire or Satisfied/ Somewhat Satisfied / Extremely Satisfied form with radio buttons or on a scale of 1 to 5. We need to ensure that the format used is very professional.<br/><br/>An optional text box for the user to enter the comment in a free format.<br/><br/>This can be done in 4 different screens or in one single screen if it does not give a clumsy look.<br/><br/>A Send button at the end to submit the Survey.<br/><br/>We need a burger menu at the top left corner of this screen, which when expanded will provide 5 options:<br/>Edit User Profile<br/>Survey interval Timer<br/>FAQ<br/>Exit<br/>About<br/><br/><br/>Please ensure that the app is simple, friendly, lively and professional at the same time so that it ignites an interest in the user to use the app.<br/>Use Logo as appropriate.
Telecommunications
Colors
Designer to choose colors to be used in the design.

```html
<!DOCTYPE html>
<html lang="en">
<head>
<meta charset="utf-8">
<title>Survey App Screens</title>
<link href="https://fonts.googleapis.com/css2?family=Roboto+Condensed:wght@300;400;700&family=Inter:wght@400;500;600&display=swap" rel="stylesheet">
<style>
  :root {
    --bg: #d4d7ea;
    --teal: #7fd6ea;
    --teal-deep: #6dc8de;
    --teal-text: #46aac4;
    --ink: #1f1f1f;
    --muted: #5a6a70;
    --paper: #ffffff;
    --mist: #ededed;
    --line: #333333;
  }
  * { box-sizing: border-box; margin: 0; padding: 0; }
  html, body { width: 1200px; height: 900px; overflow: hidden; background: var(--bg); }
  body { position: relative; font-family: "Roboto Condensed", sans-serif; color: var(--ink); }

  .screen {
    position: absolute; top: 90px; width: 330px; height: 720px;
    border-radius: 36px; overflow: hidden; background: var(--paper);
    box-shadow: 0 10px 30px rgba(80, 90, 140, 0.18);
  }
  .screen--profile { left: 75px; background: var(--mist); }
  .screen--register { left: 435px; font-family: "Inter", sans-serif; }
  .screen--survey { left: 795px; }

  .status { position: absolute; top: 14px; left: 22px; right: 22px; display: flex; justify-content: space-between; font-size: 12px; font-weight: 500; z-index: 3; }
  .status__icons { display: flex; gap: 4px; align-items: center; }

  /* Profile */
  .profile__wave { position: absolute; left: 0; top: 0; width: 330px; height: 720px; }
  .profile__bar { position: absolute; top: 40px; left: 16px; right: 16px; display: flex; justify-content: space-between; align-items: center; }
  .profile__title { font-size: 20px; font-weight: 400; letter-spacing: 0.5px; }
  .profile__card { position: absolute; top: 150px; left: 20px; width: 290px; height: 250px; background: #e9e9e9; box-shadow: 0 4px 10px rgba(0,0,0,0.12); text-align: center; }
  .profile__avatar { position: absolute; top: 100px; left: 117px; width: 96px; height: 96px; border-radius: 50%; background: var(--teal-deep); z-index: 2; }
  .profile__name { margin-top: 108px; font-size: 19px; color: var(--teal-text); }
  .profile__bio { margin: 8px auto 0; width: 220px; font-size: 13px; font-weight: 300; line-height: 1.5; }
  .profile__stats { position: absolute; bottom: 0; left: 0; right: 0; height: 50px; display: flex; border-top: 1px solid #d0d0d0; }
  .stat { flex: 1; display: flex; flex-direction: column; justify-content: center; font-size: 10px; font-weight: 300; border-right: 1px solid #d0d0d0; }
  .stat:last-child { border-right: none; }
  .stat__value { color: var(--teal-text); }
  .about { position: absolute; top: 440px; left: 20px; width: 290px; }
  .about__title { font-size: 16px; font-weight: 700; margin-bottom: 12px; }
  .about__text { font-size: 10px; font-weight: 300; line-height: 1.85; color: #2d4a52; }
  .about__text strong { font-weight: 400; color: var(--ink); }
  .faq { position: absolute; top: 610px; left: 10px; width: 310px; height: 270px; background: #f0f0f0; padding: 18px 14px; }
  .faq__title { font-size: 15px; font-weight: 700; color: var(--teal-text); margin-bottom: 18px; }
  .faq__item { border-bottom: 1px solid var(--line); padding: 6px 0 8px; font-size: 10px; font-weight: 300; display: flex; justify-content: space-between; }
  .faq__item--open { display: block; }
  .faq__head { display: flex; justify-content: space-between; }
  .faq__answer { font-size: 5.5px; line-height: 1.5; margin-top: 6px; }

  /* Register */
  .register__bg { position: absolute; inset: 0; width: 330px; height: 720px; }
  .brand { position: absolute; top: 70px; left: 0; right: 0; text-align: center; }
  .brand__mark { width: 110px; height: 110px; border-radius: 50%; background: #ffffff; box-shadow: 0 3px 10px rgba(0,0,0,0.1); margin: 0 auto 22px; }
  .brand__name { font-size: 21px; font-weight: 500; letter-spacing: 3px; line-height: 1.3; color: var(--ink); }
  .form { position: absolute; top: 372px; left: 24px; right: 24px; }
  .field { height: 40px; background: #f9f9f9; margin-bottom: 22px; box-shadow: 0 2px 5px rgba(0,0,0,0.12); font-size: 7.5px; font-weight: 600; padding: 16px 14px; }
  .btn-register { height: 40px; background: #232323; color: #fff; font-size: 12px; font-weight: 500; letter-spacing: 0.5px; display: flex; align-items: center; justify-content: center; margin-top: 4px; }
  .consent { margin-top: 22px; display: flex; align-items: center; gap: 8px; font-size: 11px; color: var(--ink); }
  .consent__box { width: 10px; height: 10px; background: #fff; }
  .consent strong { font-weight: 600; }

  /* Survey */
  .survey__ghost { position: absolute; top: 30px; left: 0; right: 0; text-align: center; font-size: 76px; font-weight: 700; color: #f2f2f2; letter-spacing: 1px; }
  .survey__title { position: absolute; top: 62px; left: 0; right: 0; text-align: center; font-size: 18px; z-index: 2; }
  .survey__list { position: absolute; top: 118px; left: 10px; right: 10px; }
  .topic { position: relative; height: 118px; margin-bottom: 24px; background: linear-gradient(100deg, var(--teal-deep), var(--teal)); box-shadow: 0 4px 10px rgba(0,0,0,0.12); overflow: hidden; color: #fff; text-align: center; }
  .topic__ghost { position: absolute; left: 4px; bottom: 2px; font-size: 34px; color: rgba(255,255,255,0.18); white-space: nowrap; }
  .topic__art { position: absolute; right: 10px; top: 10px; width: 90px; height: 100px; border-radius: 45px 45px 10px 10px; background: rgba(255,255,255,0.08); }
  .topic__icon { position: relative; margin: 16px auto 0; width: 56px; height: 56px; }
  .topic__icon--fill { border-radius: 8px; background: rgba(255,255,255,0.28); }
  .topic__label { position: relative; margin-top: 10px; font-size: 15px; }
</style>
</head>
<body>

<section class="screen screen--profile">
  <svg class="profile__wave" viewBox="0 0 330 720" aria-hidden="true">
    <path d="M0 270 Q165 370 330 250 L330 720 L0 720 Z" fill="#7fd6ea"/>
  </svg>
  <div class="status"><span>9:41</span>
    <span class="status__icons">
      <svg width="14" height="9"><rect x="0" y="6" width="2" height="3"/><rect x="4" y="4" width="2" height="5"/><rect x="8" y="2" width="2" height="7"/><rect x="12" y="0" width="2" height="9"/></svg>
      <svg width="18" height="9"><rect x="0" y="0" width="15" height="9" rx="2" fill="#1f1f1f"/></svg>
    </span>
  </div>
  <div class="profile__bar">
    <svg width="10" height="10" aria-label="Menu"><g fill="#333"><rect x="0" y="0" width="2.5" height="2.5"/><rect x="3.7" y="0" width="2.5" height="2.5"/><rect x="7.4" y="0" width="2.5" height="2.5"/><rect x="0" y="3.7" width="2.5" height="2.5"/><rect x="3.7" y="3.7" width="2.5" height="2.5"/><rect x="7.4" y="3.7" width="2.5" height="2.5"/><rect x="0" y="7.4" width="2.5" height="2.5"/><rect x="3.7" y="7.4" width="2.5" height="2.5"/><rect x="7.4" y="7.4" width="2.5" height="2.5"/></g></svg>
    <h1 class="profile__title">PROFILE</h1>
    <svg width="26" height="14" aria-label="Account and timer"><circle cx="5" cy="4" r="3" fill="#333"/><path d="M0 13 Q5 6 10 13 Z" fill="#333"/><circle cx="20" cy="8" r="5" fill="none" stroke="#333" stroke-width="1.3"/><line x1="20" y1="8" x2="20" y2="5" stroke="#333" stroke-width="1.3"/></svg>
  </div>
  <div class="profile__avatar" role="img" aria-label="User profile photo"></div>
  <div class="profile__card">
    <h2 class="profile__name">CLARA BENTON</h2>
    <p class="profile__bio">Lorem Ipsum is simply dummy text of the printing and typesetting industry</p>
    <div class="profile__stats">
      <div class="stat"><span class="stat__value">236</span><span>Records</span></div>
      <div class="stat"><span class="stat__value">23,6k</span><span>Ratings</span></div>
      <div class="stat"><span class="stat__value">2,8k</span><span>Records</span></div>
    </div>
  </div>
  <div class="about">
    <h3 class="about__title">About</h3>
    <p class="about__text">Lorem Ipsum is simply dummy text of the printing and typesetting industry. Lorem Ipsum has been the industry's standard dummy text ever since the 1500s, <strong>when an unknown printer took a galley of type and scrambled it to make a type specimen book.</strong> It has survived not only five centuries, but also the leap into electronic typesetting, remaining essentially unchanged.</p>
  </div>
  <div class="faq">
    <h3 class="faq__title">FAQ'S</h3>
    <div class="faq__item faq__item--open">
      <div class="faq__head"><span>Lorem Ipsum is simply dummy text of the printing</span><span>-</span></div>
      <p class="faq__answer">Lorem Ipsum is simply dummy text of the printing and typesetting industry. Lorem Ipsum has been the industry's standard dummy text ever since the 1500s, when an unknown printer took a galley of type and scrambled it to make a type specimen book.</p>
    </div>
    <div class="faq__item"><span>Lorem Ipsum is simply dummy text</span><span>+</span></div>
    <div class="faq__item"><span>Lorem Ipsum is simply dummy text of the printing</span><span>+</span></div>
  </div>
</section>

<section class="screen screen--register">
  <svg class="register__bg" viewBox="0 0 330 720" aria-hidden="true">
    <path d="M0 270 Q165 380 330 270 L330 720 L0 720 Z" fill="#7fd6ea"/>
    <path d="M0 290 Q110 330 100 520 Q90 640 0 720 Z" fill="#74cee3"/>
    <path d="M330 520 Q240 600 260 720 L330 720 Z" fill="#74cee3"/>
  </svg>
  <div class="status"><span>9:41</span>
    <span class="status__icons">
      <svg width="14" height="9"><rect x="0" y="6" width="2" height="3"/><rect x="4" y="4" width="2" height="5"/><rect x="8" y="2" width="2" height="7"/><rect x="12" y="0" width="2" height="9"/></svg>
      <svg width="18" height="9"><rect x="0" y="0" width="15" height="9" rx="2" fill="#1f1f1f"/></svg>
    </span>
  </div>
  <div class="brand">
    <div class="brand__mark"></div>
    <p class="brand__name">MERIDIAN<br>LABS</p>
  </div>
  <form class="form">
    <div class="field">Name</div>
    <div class="field">Phone Number</div>
    <div class="field">Group Number</div>
    <div class="field">Information</div>
    <div class="btn-register">REGISTER</div>
    <div class="consent"><span class="consent__box"></span><span><strong>Registering</strong> I agree to participate in the Survey</span></div>
  </form>
</section>

<section class="screen screen--survey">
  <div class="status"><span>9:41</span>
    <span class="status__icons">
      <svg width="14" height="9"><rect x="0" y="6" width="2" height="3"/><rect x="4" y="4" width="2" height="5"/><rect x="8" y="2" width="2" height="7"/><rect x="12" y="0" width="2" height="9"/></svg>
      <svg width="18" height="9"><rect x="0" y="0" width="15" height="9" rx="2" fill="#1f1f1f"/></svg>
    </span>
  </div>
  <div class="survey__ghost" aria-hidden="true">SURVEY</div>
  <h1 class="survey__title">SURVEY</h1>
  <div class="survey__list">
    <div class="topic">
      <span class="topic__ghost" aria-hidden="true">Call Experience</span>
      <div class="topic__art" role="img" aria-label="Support agent illustration"></div>
      <div class="topic__icon topic__icon--fill" role="img" aria-label="Call agent icon"></div>
      <p class="topic__label">Call Experience</p>
    </div>
    <div class="topic">
      <span class="topic__ghost" aria-hidden="true">Call Experience</span>
      <div class="topic__art" role="img" aria-label="Support agent illustration"></div>
      <svg class="topic__icon" viewBox="0 0 56 56" aria-label="Message icon"><rect x="6" y="10" width="44" height="32" fill="none" stroke="#fff" stroke-width="2.5"/><path d="M6 10 L28 30 L50 10" fill="none" stroke="#fff" stroke-width="2.5"/></svg>
      <p class="topic__label">SMS Experience</p>
    </div>
    <div class="topic">
      <span class="topic__ghost" aria-hidden="true">Call Experience</span>
      <div class="topic__art" role="img" aria-label="Support agent illustration"></div>
      <svg class="topic__icon" viewBox="0 0 56 56" aria-label="Data window icon"><rect x="6" y="8" width="44" height="38" fill="none" stroke="#fff" stroke-width="2.5"/><line x1="6" y1="16" x2="50" y2="16" stroke="#fff" stroke-width="2"/><line x1="12" y1="24" x2="40" y2="24" stroke="#fff" stroke-width="2"/><line x1="12" y1="31" x2="44" y2="31" stroke="#fff" stroke-width="2"/><line x1="12" y1="38" x2="34" y2="38" stroke="#fff" stroke-width="2"/></svg>
      <p class="topic__label">Data Experience</p>
    </div>
    <div class="topic">
      <span class="topic__ghost" aria-hidden="true">Call Experience</span>
      <div class="topic__art" role="img" aria-label="Support agent illustration"></div>
      <svg class="topic__icon" viewBox="0 0 56 56" aria-label="Rating list icon"><path d="M10 10 l2.5 5 5.5 0.8 -4 3.8 1 5.4 -5 -2.6 -5 2.6 1 -5.4 -4 -3.8 5.5 -0.8z" fill="#fff"/><path d="M10 32 l2.5 5 5.5 0.8 -4 3.8 1 5.4 -5 -2.6 -5 2.6 1 -5.4 -4 -3.8 5.5 -0.8z" fill="#fff"/><rect x="24" y="12" width="28" height="3" fill="#fff"/><rect x="24" y="20" width="28" height="3" fill="#fff"/><rect x="24" y="34" width="28" height="3" fill="#fff"/><rect x="24" y="42" width="28" height="3" fill="#fff"/></svg>
      <p class="topic__label">Streaming Experience</p>
    </div>
  </div>
</section>

</body>
</html>
```